BuildLinkHub.com Full Stationery Design

Business Card will have all info on it. Letterhead will not have name, title or mobile number. Keep general feeling very clean, using colors from the logo as accents.
Name:Dale Morrisette
Title:President
Phone: 1-800-555-0142
Cell: 306-555-0179
email: dale@buildlinkhub.example
website: www.buildlinkhub.example
Address:
PO Box 872
Cedar Bend, PR
S0J2T0

Target Market(s)

Construction Business owners

Industry/Entity Type

Business

Contact Information for Business Card

Name:Dale Morrisette
Title:President
Phone: 1-800-555-0142
Cell: 306-555-0179
Address:
PO Box 872
Cedar Bend, PR
S0J2T0

Font styles to use
Sans Serif

Requirements
Must have
• Clean look
Should not have
• Images or cartoon type characters or tools

```html
<!DOCTYPE html>
<html lang="en">
<head>
<meta charset="utf-8">
<title>BuildLinkHub.com Stationery</title>
<link rel="stylesheet" href="https://fonts.googleapis.com/css2?family=Open+Sans:wght@400;600&display=swap">
<style>
  :root {
    --slate: #4e5a68;
    --red: #e8202e;
    --orange: #f05a28;
    --ink: #3a4350;
    --paper: #ffffff;
    --backdrop: #e9e9e9;
    --corner-fill: linear-gradient(135deg, #55606e 0%, #6b7785 45%, #e8402a 75%, #f26522 100%);
  }
  * { box-sizing: border-box; margin: 0; padding: 0; }
  html, body { width: 1200px; height: 1000px; overflow: hidden; }
  body {
    position: relative;
    background: var(--backdrop);
    font-family: "Open Sans", sans-serif;
    color: var(--ink);
  }
  .sheet, .card {
    position: absolute;
    background: var(--paper);
    overflow: hidden;
    box-shadow: 0 1px 3px rgba(0,0,0,.12);
  }
  .sheet { width: 454px; height: 641px; top: 77px; }
  .sheet--blank { left: 131px; }
  .sheet--letter { left: 611px; }

  .corner-art { position: absolute; top: 0; right: 0; background: var(--corner-fill); }
  .sheet .corner-art { width: 170px; height: 140px; }
  .card .corner-art { width: 130px; height: 92px; }

  .wordmark {
    font-weight: 600;
    color: var(--slate);
    letter-spacing: .2px;
    white-space: nowrap;
  }
  .wordmark__square {
    display: inline-block;
    background: var(--orange);
    vertical-align: middle;
  }
  .sheet .wordmark { position: absolute; left: 22px; top: 30px; font-size: 19px; }
  .sheet .wordmark__square { width: 14px; height: 14px; margin-right: 7px; margin-top: -3px; }

  .contact { position: absolute; font-size: 7.2px; line-height: 11px; color: var(--ink); }
  .contact__row { display: flex; align-items: center; gap: 4px; white-space: nowrap; }
  .icon { width: 7px; height: 7px; flex: none; }
  .sheet .contact--web { left: 24px; top: 94px; }
  .sheet .contact--post { left: 180px; top: 95px; }
  .contact--post .contact__indent { padding-left: 11px; }

  .letter__to { position: absolute; left: 26px; top: 222px; font-size: 8px; }
  .letter__body { position: absolute; left: 23px; top: 295px; width: 408px; font-size: 6.8px; line-height: 10px; text-align: justify; }
  .letter__body p + p { margin-top: 10px; }
  .letter__from { position: absolute; left: 352px; top: 593px; font-size: 8px; }

  .card { width: 255px; height: 146px; top: 767px; border-radius: 10px; }
  .card--front { left: 536px; }
  .card--back { left: 809px; }

  .card__mark {
    position: absolute; left: 18px; top: 34px; width: 80px;
    font-size: 13px; line-height: 17px; font-weight: 600; color: var(--slate);
  }
  .card__name { position: absolute; left: 114px; top: 25px; font-size: 13px; font-weight: 600; color: var(--slate); }
  .card__name span { color: var(--red); }
  .card__title { position: absolute; left: 114px; top: 42px; font-size: 10px; color: var(--ink); }
  .card .contact { font-size: 7px; line-height: 9px; }
  .card .contact--web { left: 114px; top: 59px; }
  .card .contact--post { left: 114px; top: 89px; }
  .card__footer { position: absolute; left: 0; bottom: 0; width: 255px; height: 14px; }

  .card--back .wordmark { position: absolute; left: 16px; top: 100px; font-size: 14px; }
  .card--back .wordmark__square { width: 11px; height: 11px; margin-right: 5px; margin-top: -2px; }
</style>
</head>
<body>

<!-- Blank letterhead -->
<section class="sheet sheet--blank">
  <div class="corner-art" role="img" aria-label="Angular slate and red-orange corner graphic"></div>
  <div class="wordmark"><span class="wordmark__square"></span>BuildLinkHub.com</div>
  <div class="contact contact--web">
    <div class="contact__row"><svg class="icon" viewBox="0 0 10 10"><rect x="0" y="2" width="10" height="7" fill="var(--red)"/></svg>dale@buildlinkhub.example</div>
    <div class="contact__row"><svg class="icon" viewBox="0 0 10 10"><circle cx="5" cy="5" r="4.2" fill="none" stroke="var(--red)" stroke-width="1.4"/><line x1="1" y1="5" x2="9" y2="5" stroke="var(--red)"/><ellipse cx="5" cy="5" rx="1.8" ry="4.2" fill="none" stroke="var(--red)"/></svg>www.buildlinkhub.example</div>
  </div>
  <div class="contact contact--post">
    <div class="contact__row"><svg class="icon" viewBox="0 0 10 10"><path d="M5 10 L1.5 5 A3.6 3.6 0 1 1 8.5 5 Z" fill="var(--red)"/><circle cx="5" cy="3.6" r="1.3" fill="#fff"/></svg>PO Box 872, Cedar Bend</div>
    <div class="contact__indent">PR, S0J2T0</div>
  </div>
</section>

<!-- Letter sample -->
<section class="sheet sheet--letter">
  <div class="corner-art" role="img" aria-label="Angular slate and red-orange corner graphic"></div>
  <div class="wordmark"><span class="wordmark__square"></span>BuildLinkHub.com</div>
  <div class="contact contact--web">
    <div class="contact__row"><svg class="icon" viewBox="0 0 10 10"><rect x="0" y="2" width="10" height="7" fill="var(--red)"/></svg>dale@buildlinkhub.example</div>
    <div class="contact__row"><svg class="icon" viewBox="0 0 10 10"><circle cx="5" cy="5" r="4.2" fill="none" stroke="var(--red)" stroke-width="1.4"/><line x1="1" y1="5" x2="9" y2="5" stroke="var(--red)"/><ellipse cx="5" cy="5" rx="1.8" ry="4.2" fill="none" stroke="var(--red)"/></svg>www.buildlinkhub.example</div>
  </div>
  <div class="contact contact--post">
    <div class="contact__row"><svg class="icon" viewBox="0 0 10 10"><path d="M5 10 L1.5 5 A3.6 3.6 0 1 1 8.5 5 Z" fill="var(--red)"/><circle cx="5" cy="3.6" r="1.3" fill="#fff"/></svg>PO Box 872, Cedar Bend</div>
    <div class="contact__indent">PR, S0J2T0</div>
  </div>

  <div class="letter__to">To</div>
  <div class="letter__body">
    <p>Lorem ipsum dolor sit amet, consectetur adipiscing elit. In eget felis molestie, scelerisque mauris non, posuere nibh. Cras nibh eros, lobortis non varius ut, feugiat a nulla. Donec egestas scelerisque quam ut congue. Suspendisse laoreet rutrum tempus. Curabitur pretium ornare quam, at molestie magna scelerisque ut. Cras mattis turpis in justo feugiat, ac tincidunt neque ornare.</p>
    <p>Fusce vestibulum placerat elementum. Quisque congue lacus ut felis viverra hendrerit. Integer posuere tortor id eros vulputate, vel molestie elit viverra. Pellentesque convallis posuere erat ac vulputate. Nam posuere pulvinar arcu ac rhoncus. Cras efficitur consequat interdum. Aliquam in vestibulum risus.</p>
    <p>Pellentesque nisi elit, rhoncus et imperdiet ac, dapibus ut ante. Integer consectetur sem vel sem aliquet, sit amet aliquam ex vehicula. Sed eu velit diam. Phasellus imperdiet odio non sodales ullamcorper. Donec placerat, turpis a dictum aliquam, tortor nunc facilisis libero, et rutrum tellus magna a nibh. Vestibulum pulvinar laoreet nisl quis blandit. Nullam vitae velit volutpat, ultricies arcu at, pretium libero.</p>
    <p>Quisque nec dictum tellus, venenatis congue felis. Fusce vitae est sed sapien tristique aliquet nec eget lorem. In vestibulum eget ante eu finibus. Praesent malesuada blandit ante nec facilisis. Nulla accumsan nibh ut justo fringilla, vel blandit dui ornare. Sed gravida leo id leo pretium sagittis ut quis metus. Nulla interdum dignissim molestie. Donec felis ipsum, elementum sit amet nibh ut, mattis maximus mauris.</p>
    <p>Suspendisse auctor mauris egestas, congue lectus a, ornare sem. Donec ut dolor ut elit blandit pellentesque at at leo. Nullam elementum felis sit amet erat euismod gravida. Etiam rhoncus mi eu venenatis dictum. Suspendisse ut lacus magna. Ut enim est, tempor nec felis vel, viverra luctus libero. In commodo consequat vulputate. Maecenas tempus, ante ut venenatis rhoncus, justo quam ultrices magna, ut ultrices mi leo sit amet ligula.</p>
  </div>
  <div class="letter__from">From</div>
</section>

<!-- Business card front -->
<section class="card card--front">
  <div class="card__mark">BuildLink<br>Hub.com</div>
  <div class="card__name">Dale <span>Morrisette</span></div>
  <div class="card__title">President</div>
  <div class="contact contact--web">
    <div class="contact__row"><svg class="icon" viewBox="0 0 10 10"><path d="M1 4 Q5 0 9 4 L8 5.5 L6.5 4.5 L3.5 4.5 L2 5.5 Z M2 6 H8 V9 H2 Z" fill="var(--red)"/></svg>1-800-555-0142</div>
    <div class="contact__row"><svg class="icon" viewBox="0 0 10 10"><rect x="0" y="2" width="10" height="7" fill="var(--red)"/></svg>dale@buildlinkhub.example</div>
    <div class="contact__row"><svg class="icon" viewBox="0 0 10 10"><circle cx="5" cy="5" r="4.2" fill="none" stroke="var(--red)" stroke-width="1.4"/><line x1="1" y1="5" x2="9" y2="5" stroke="var(--red)"/><ellipse cx="5" cy="5" rx="1.8" ry="4.2" fill="none" stroke="var(--red)"/></svg>www.buildlinkhub.example</div>
  </div>
  <div class="contact contact--post">
    <div class="contact__row"><svg class="icon" viewBox="0 0 10 10"><path d="M5 10 L1.5 5 A3.6 3.6 0 1 1 8.5 5 Z" fill="var(--red)"/><circle cx="5" cy="3.6" r="1.3" fill="#fff"/></svg>PO Box 872, Cedar Bend</div>
    <div class="contact__indent">PR, S0J2T0</div>
  </div>
  <svg class="card__footer" viewBox="0 0 255 14" preserveAspectRatio="none" aria-hidden="true">
    <rect x="0" y="6" width="92" height="8" fill="var(--red)"/>
    <polygon points="90,14 95,0 255,0 255,14" fill="var(--slate)"/>
  </svg>
</section>

<!-- Business card back -->
<section class="card card--back">
  <div class="corner-art" role="img" aria-label="Angular slate and red-orange corner graphic"></div>
  <div class="wordmark"><span class="wordmark__square"></span>BuildLinkHub.com</div>
</section>

</body>
</html>
```